Wattlegrove Aged Care Centre

We need a website design for an aged care facility in Brisbane (a different one to project already posted) with final design provided as a .psd file.

This website will be built on Dot Net Nuke so design needs to be able to be converted into a DNN skin and containers.

Target Market(s)

• Credibility
• Family orientated
• Establish an online identity
• Download a booking form for tours
• Receive general enquiries
• Feature a phone number
• Advertise career opportunities

Number of Pages Required

1 page

Requirements
Must have
• o The following elements are to be included in the design concepts:
• o Phone number will be featured in banner 07 3821 4476
• o Logo and words Marstow Care Centre to be featured in banner
• o Area for a flash banner of rotating images on homepage (have attached some images)
• o 3 x buttons to be designed and feature on homepage - Book a Tour, Contact Us and Sign up to our newsletter
• o No colour preference but perhaps keeping with their logo/branding but am open to ideas

```html
<!DOCTYPE html>
<html lang="en">
<head>
<meta charset="utf-8">
<title>Wattlegrove Aged Care Centre – Facilities</title>
<link rel="stylesheet" href="https://fonts.googleapis.com/css2?family=Tinos:wght@400;700&family=Arimo:wght@400;700&display=swap">
<style>
  :root{
    --cream:#f3f1e8;
    --band:#e6d6bb;
    --band-dark:#d8c3a0;
    --content-top:#f1ead2;
    --content-bottom:#e6dbb5;
    --side-strip:#e3d9c1;
    --nav-text:#8b2412;
    --heading:#a8431f;
    --body-text:#2b2418;
    --green:#1f4f2a;
    --panel-top:#c9c7c2;
    --panel-bottom:#a9a6a0;
    --footer-top:#fbf6ea;
    --footer-bottom:#efe2c6;
    --chocolate:#3a2414;
    --highlight:#cfd2c2;
    --link:#b0541c;
  }
  *{box-sizing:border-box;margin:0;padding:0}
  html,body{width:1177px;height:1200px;overflow:hidden;background:var(--cream)}
  body{position:relative;font-family:"Arimo",Arial,sans-serif;color:var(--body-text)}

  .hero{position:absolute;left:0;top:0;width:1177px;height:415px;
    background:linear-gradient(180deg,#8e9a8c 0%,#7a6a55 35%,#5d5a45 65%,#8c8a80 85%,#a9a7a0 100%)}
  .hero-band{position:absolute;left:0;top:415px;width:1177px;height:25px;
    background:linear-gradient(180deg,var(--band-dark),var(--band) 40%,#f1e6d2)}

  .main-nav{position:absolute;left:0;top:440px;width:1177px;height:75px;background:var(--band);display:flex}
  .nav-tab{position:relative;width:189px;height:72px;display:flex;align-items:center;justify-content:center;
    font-family:"Tinos",serif;font-size:19px;color:var(--nav-text);text-transform:uppercase;
    background:linear-gradient(180deg,#fbfaf5,#e9e7dc);border-right:1px solid #cfc9b6;text-decoration:none}
  .nav-tab::after{content:"";position:absolute;right:0;bottom:0;width:14px;height:14px;
    background:linear-gradient(135deg,#b8b3a2 0 50%,var(--band) 50%)}
  .nav-tab.is-active{height:78px;background:linear-gradient(180deg,#fbfaf5,#f3f1e8)}
  .nav-tab.is-active::after{display:none}
  .nav-tab:last-child{width:188px}

  .sidebar{position:absolute;left:0;top:515px;width:380px;height:340px;background:var(--cream)}
  .brand{position:absolute;left:0;top:50px;width:380px;text-align:center}
  .brand-mark{width:36px;height:36px;border-radius:50%;background:var(--green);margin:0 auto 14px}
  .brand-name{font-family:"Tinos",serif;font-size:24px;color:var(--green);line-height:1.2;padding:0 40px}
  .phone{position:absolute;left:0;top:240px;width:380px;text-align:center;font-family:"Tinos",serif;font-size:31px;color:var(--green)}

  .tour-panel{position:absolute;left:0;top:855px;width:380px;height:224px;
    background:linear-gradient(180deg,var(--panel-top),var(--panel-bottom))}
  .tour-photo{position:absolute;left:22px;top:32px;width:139px;height:152px;border:1px solid #6a665e;
    background:linear-gradient(160deg,#bfae8c,#8a6f49 45%,#4e443a)}
  .tour-title{position:absolute;left:180px;top:30px;font-family:"Tinos",serif;color:var(--heading);font-size:33px;line-height:1}
  .tour-title small{font-size:27px;color:#6b2a14}
  .tour-text{position:absolute;left:182px;top:76px;width:195px;font-size:16px;font-weight:700;line-height:21px;color:#2a2018;white-space:nowrap}
  .more-info{position:absolute;left:184px;top:151px;width:142px;height:36px;background:linear-gradient(180deg,#fff,#e6e4dc);
    border:1px solid #8d887c;color:var(--nav-text);font-size:17px;font-weight:700;display:flex;align-items:center;justify-content:center;text-decoration:none}

  .content{position:absolute;left:380px;top:515px;width:754px;height:564px;
    background:linear-gradient(180deg,var(--content-top),var(--content-bottom))}
  .side-strip{position:absolute;left:1134px;top:440px;width:43px;height:639px;background:var(--side-strip);border-left:2px solid #c8bfa9}
  .content h1{position:absolute;left:212px;top:30px;font-family:"Tinos",serif;font-weight:400;font-size:31px;color:var(--heading)}
  .content-body{position:absolute;left:53px;top:126px;width:650px;font-size:15px;line-height:20px}
  .content-body p{margin-bottom:20px}
  .content-photo{position:absolute;top:392px;width:227px;height:152px;border:1px solid #3f5a33}
  .photo-resident{left:61px;background:linear-gradient(160deg,#d8d0bd,#c7b79a 50%,#a9a27f)}
  .photo-dining{left:325px;background:linear-gradient(180deg,#3c4a5c,#6c7686 45%,#c7cad0)}

  .submenu{position:absolute;left:380px;top:518px;width:187px;background:var(--cream);list-style:none}
  .submenu li{height:37px;display:flex;align-items:center;justify-content:center;font-family:"Tinos",serif;font-size:18px;color:var(--nav-text);text-transform:uppercase}
  .submenu li.is-current{background:var(--highlight)}

  .footer-band{position:absolute;left:0;top:1079px;width:1177px;height:20px;
    background:linear-gradient(180deg,#e6d2b0,#cfb58c 50%,#f1e5cf)}
  .footer{position:absolute;left:0;top:1099px;width:1177px;height:101px;
    background:linear-gradient(180deg,var(--footer-top),var(--footer-bottom))}
  .footer-mark{position:absolute;left:72px;top:30px;width:58px;height:42px;border-radius:50%;background:#ddd3c0}
  .footer-links{position:absolute;left:230px;top:27px;display:flex;font-size:16px;color:#111;list-style:none}
  .footer-links li+li::before{content:":";color:var(--link);margin:0 19px}
  .copyright{position:absolute;left:420px;top:53px;font-size:16px;color:#111}
  .copyright a{color:var(--link)}
  .footer-corner{position:absolute;left:1134px;top:1099px;width:43px;height:101px;background:var(--chocolate)}
</style>
</head>
<body>
  <div class="hero" role="img" aria-label="Photograph of the brick care centre building with ramp railings and tropical garden"></div>
  <div class="hero-band"></div>

  <nav class="main-nav">
    <a class="nav-tab" href="#">Home</a>
    <a class="nav-tab" href="#">About Us</a>
    <a class="nav-tab is-active" href="#">Facilities</a>
    <a class="nav-tab" href="#">Tours</a>
    <a class="nav-tab" href="#">Careers</a>
    <a class="nav-tab" href="#">Contact Us</a>
  </nav>
  <div class="side-strip"></div>

  <aside class="sidebar">
    <div class="brand">
      <div class="brand-mark"></div>
      <div class="brand-name">Wattlegrove Aged Care Centre</div>
    </div>
    <div class="phone">07 3821 4476</div>
  </aside>

  <section class="tour-panel">
    <div class="tour-photo" role="img" aria-label="Photograph of a bright resident kitchen"></div>
    <div class="tour-title">BOOK A <small>tour</small></div>
    <p class="tour-text">Lorem ipsum dolor<br>sit amet consectetur<br>adipi sitsicingt</p>
    <a class="more-info" href="#">more info</a>
  </section>

  <main class="content">
    <h1>FACILITIES</h1>
    <div class="content-body">
      <p>To make your transition as smooth as possible, our suites are fully furnished. However, your own personal touch is welcomed, so feel free to complete finishing touches with your own prized possessions. The choice is yours!</p>
      <p>Each suite was designed and built with your safety and comfort as a top priority. At Wattlegrove we offer countless amenities all within the confines of your own home.</p>
      <p>We have elegantly decorated lounges and common areas ideal for quiet relaxation. You can have a seat and chat with family and friends or sit and watch your favourite program on our TV. A large cheerful dining room allows you to socialize with fellow residents while enjoying your meals. You can also peacefully sip your cup of tea on our spacious patio and enjoy the picturesque view of Random Sound. Your lifestyle is waiting at the Wattlegrove.</p>
    </div>
    <div class="content-photo photo-resident" role="img" aria-label="Photograph of a smiling resident"></div>
    <div class="content-photo photo-dining" role="img" aria-label="Photograph of the dining room set with tables"></div>
  </main>

  <ul class="submenu">
    <li>Security</li>
    <li class="is-current">Housekeeping</li>
    <li>Transportation</li>
  </ul>

  <div class="footer-band"></div>
  <footer class="footer">
    <div class="footer-mark" role="img" aria-label="Faint bird illustration"></div>
    <ul class="footer-links">
      <li>Home</li><li>About Us</li><li>Facilities</li><li>Tours</li><li>Careers</li><li>Contacts</li>
    </ul>
    <p class="copyright">2009 | &nbsp;<a href="#">Privacy policy</a></p>
  </footer>
  <div class="footer-corner"></div>
</body>
</html>
```